Design clean technology service-based company website

Hello, We are looking to reskin our company website. We are an environmental inspection company and test for Asbestos, Lead and Mold along with other contaminants. People depend on the results to be accurate and fast. We are regulated by the NQB and State regulations. We work a lot with business to business and business to customer. We are wanting to make our new presentation to be modern and easy for customers to interact with us, understand our process and services while providing valuable environmental informational resource and updates. We are a technology based company and will be providing instantaneous results as reports come in for the customers. We are needing good calls to action on the site to direct them to setup a new inspection. Each user will have a backend access to their job information with invoices, reports, status, etc. We have developed software to be able to proved these reports and want to look the part.

My current website is www.trylumaverde.com
Updates

Helllo we are wanting to make sure we have good time to select the right website for us and also have the additional time to select other pages of the website. We have received great designs and have consolidated our requests into a document for the next set of iterations.

Target Market(s)

Home Owners, Contractors, Engineers, Real Estate Agents, Building Owners, Insurance Adjusters

Industry/Entity Type

Environmental Consultant

Number of Pages Required

5+ page

Font styles to use
Sans Serif

Colors
0355a3
9bcb3c
7f7f7f
f5f5f5
000000

Requirements
Must have
• Use our existing logo to design around
• The layouts look good in mobile mode for understanding and selecting services and signing up
• Clean Modern Layout
• Have all pages on the website have a similar layout and feel
• Clearly communicate services along with bundle service packages
• Detail the customer journey with graphic design
• Great call to actions to either schedule inspection online, call, text, chat
Nice to have
• Have an interactive graphic for where to test for lead, asbestos and mold.
• I like the becky barlows top order line bar - see attached
• Have clear question and answer page layouts for asbestos, lead and mold
• Show Company reviews
• Have clear Resources pages for all types of contaminants
Should not have
• My current website is www.trylumaverde.com

```html
<!DOCTYPE html>
<html lang="en">
<head>
<meta charset="utf-8">
<title>Lumaverde Environmental Inspections</title>
<link href="https://fonts.googleapis.com/css2?family=Open+Sans:wght@400;600;700&display=swap" rel="stylesheet">
<style>
:root{
  --blue:#0355a3;
  --green:#6fb52c;
  --lime:#9bcb3c;
  --grey:#7f7f7f;
  --light:#f5f5f5;
  --panel:#e6e6e6;
  --ink:#333333;
  --black:#000000;
  --white:#ffffff;
}
*{box-sizing:border-box;margin:0;padding:0}
html,body{width:1200px;height:3364px;overflow:hidden}
body{font-family:"Open Sans",Arial,sans-serif;color:var(--ink);background:var(--white);position:relative}
section,header,footer{position:absolute;left:0;width:1200px}
.btn{position:absolute;display:flex;align-items:center;justify-content:center;background:var(--blue);color:var(--white);font-weight:600;font-size:16px;text-transform:uppercase;letter-spacing:.3px}
.heading{color:var(--green);font-weight:700;text-transform:uppercase;font-size:30px;letter-spacing:.3px;line-height:38px}

/* hero */
.hero{top:0;height:550px}
.hero-photo{position:absolute;inset:0;background:linear-gradient(100deg,#4a4d4f 0%,#7b7f80 22%,#c9cbc6 45%,#e3e4df 70%,#d6d8d2 100%)}
.brand{position:absolute;left:85px;top:26px;display:flex;align-items:center;gap:12px}
.brand-mark{width:22px;height:22px;border-radius:50%;background:var(--green)}
.brand-name{font-size:40px;font-weight:700;color:var(--green);letter-spacing:.5px;line-height:50px}
.topbar{position:absolute;right:85px;top:16px;display:flex;gap:28px;font-size:16px;color:var(--ink)}
.topbar span{display:flex;align-items:center;gap:8px}
.nav{position:absolute;right:85px;top:52px;display:flex;gap:4px}
.nav a{font-size:15px;font-weight:600;color:var(--ink);padding:4px 9px;text-decoration:none;text-transform:uppercase}
.nav a.active{background:var(--green);color:var(--white)}
.hero-copy{position:absolute;right:85px;top:196px;text-align:right}
.hero-kicker{color:var(--lime);font-size:20px;font-weight:600;text-transform:uppercase;line-height:24px}
.hero-places{color:var(--green);font-size:31px;font-weight:700;line-height:32px;text-transform:uppercase}
.hero-sub{color:#555;font-size:15px;font-weight:600;margin-top:10px;line-height:20px}
.hero .btn{right:85px;top:380px;width:233px;height:42px}
.dots{position:absolute;left:576px;top:526px;display:flex;gap:6px}
.dots i{width:12px;height:12px;border-radius:50%;background:var(--white)}
.dots i:first-child{background:var(--green)}

/* about */
.about{top:550px;height:482px}
.about .heading{position:absolute;left:85px;top:80px}
.about-text{position:absolute;left:85px;top:132px;width:565px;font-size:13.5px;line-height:21px;color:#444}
.about-text p+p{margin-top:18px}
.about .btn{left:85px;top:354px;width:145px;height:40px}
.about-photo{position:absolute;left:700px;top:60px;width:415px;height:360px;background:linear-gradient(160deg,#3d79c4 0%,#86a9cf 35%,#8a8e86 55%,#4f6a36 100%);box-shadow:0 8px 18px rgba(0,0,0,.35)}

/* project band */
.project{top:1032px;height:323px;background:linear-gradient(135deg,#222 0%,#3e3c36 45%,#2a2a2a 100%);text-align:center}
.project svg{position:absolute;left:578px;top:76px}
.project .heading{position:absolute;top:126px;width:100%}
.project p{position:absolute;top:168px;left:100px;width:1000px;color:var(--white);font-size:16px;line-height:24px}
.project .btn{left:530px;top:230px;width:140px;height:40px}

/* services */
.services{top:1355px;height:451px}
.services .heading{position:absolute;top:52px;width:100%;text-align:center}
.tabs{position:absolute;left:260px;top:112px;display:flex}
.tabs span{width:230px;height:36px;display:flex;align-items:center;justify-content:center;font-size:15px;text-transform:uppercase;background:#e9e9e9;color:#444}
.tabs span.active{background:var(--blue);color:var(--white)}
.services-text{position:absolute;left:85px;top:193px;width:505px;font-size:13.5px;line-height:21px;color:#444}
.services-photo{position:absolute;left:612px;top:179px;width:503px;height:209px;background:linear-gradient(180deg,#f2f2f2 0%,#b9bcbd 50%,#6f7273 100%)}

/* why */
.why{top:1806px;height:464px;background:linear-gradient(160deg,#262626 0%,#141414 60%,#1f1f1f 100%);color:var(--white)}
.why .heading{position:absolute;left:85px;top:54px}
.reason{position:absolute;left:85px;width:1030px}
.reason h3{display:flex;align-items:center;gap:14px;font-size:15px;font-weight:700;text-transform:uppercase}
.reason p{font-size:13.5px;line-height:21px;margin-top:10px}

/* certificates */
.proof{top:2270px;height:460px}
.card{position:absolute;top:58px;width:503px;height:341px;background:var(--panel)}
.card h2{height:49px;background:var(--blue);color:var(--white);font-size:31px;font-weight:600;text-transform:uppercase;display:flex;align-items:center;justify-content:center}
.cert{left:85px}
.badge{position:absolute;background:#9c9c9c}
.journey{left:612px;text-align:center}
.journey .date{margin-top:22px;font-size:17px;color:#444}
.journey .stars{margin-top:4px}
.journey .quote{font-size:44px;color:#aaa;line-height:30px;margin-top:8px}
.journey p{width:380px;margin:6px auto 0;font-size:14px;line-height:21px;color:#555}
.journey .by{margin-top:20px;font-size:14px;display:flex;gap:8px;justify-content:center;align-items:center}
.journey .btn{left:178px;top:276px;width:145px;height:40px}

.map{top:2730px;height:357px;background:linear-gradient(135deg,#e7e4df 0%,#f1efea 50%,#e1ddd4 100%)}

/* footer */
.footer{top:3087px;height:249px;background:var(--blue);color:var(--white)}
.fcol{position:absolute;top:46px}
.fcol h4{font-size:16px;font-weight:700;text-transform:uppercase;margin-bottom:10px;line-height:22px}
.fcol li{list-style:none;font-size:13px;line-height:21px;display:flex;align-items:center;gap:10px}
.fcol .contact li{margin-bottom:8px;align-items:flex-start}
.field{width:325px;height:30px;border:1px solid #3b7dc2;background:#0a4d93;color:#d9e6f4;font-size:13px;padding:6px 8px;margin-bottom:7px;line-height:16px}
.field.message{width:295px;height:56px}
.send{position:absolute;right:0;top:106px;width:28px;height:56px;background:#1f6fc0;display:flex;align-items:center;justify-content:center}
.legal{position:absolute;left:0;width:1200px;top:3336px;height:28px;background:var(--green);color:var(--white);font-size:13px;display:flex;align-items:center;justify-content:center}
</style>
</head>
<body>

<header class="hero">
  <div class="hero-photo" role="img" aria-label="Photo of a hand holding a moisture meter against a weathered wall"></div>
  <div class="brand"><span class="brand-mark"></span><span class="brand-name">Lumaverde</span></div>
  <div class="topbar">
    <span><svg width="18" height="18" viewBox="0 0 24 24"><path fill="#0355a3" d="M6.6 10.8a15 15 0 0 0 6.6 6.6l2.2-2.2c.3-.3.7-.4 1-.2 1.1.4 2.3.6 3.6.6.6 0 1 .4 1 1V20c0 .6-.4 1-1 1A17 17 0 0 1 3 4c0-.6.4-1 1-1h3.5c.6 0 1 .4 1 1 0 1.3.2 2.5.6 3.6.1.3 0 .7-.2 1z"/></svg>303 555 0147</span>
    <span><svg width="20" height="16" viewBox="0 0 20 16"><rect x="1" y="1" width="18" height="14" fill="#0355a3"/><path d="M1 1l9 7 9-7" stroke="#fff" stroke-width="1.5" fill="none"/></svg>info@trylumaverde.com</span>
    <span><svg width="20" height="18" viewBox="0 0 20 18"><rect x="1" y="3" width="18" height="14" fill="none" stroke="#0355a3" stroke-width="2"/><rect x="1" y="3" width="18" height="4" fill="#0355a3"/></svg>Same Day response</span>
  </div>
  <nav class="nav">
    <a class="active">Home</a><a>Our Services</a><a>Resources</a><a>Blog</a><a>Q &amp; A</a><a>Reviews</a><a>Connect</a>
  </nav>
  <div class="hero-copy">
    <div class="hero-kicker">Proudly Serving</div>
    <div class="hero-places">Denver<br>Colorado Springs<br>Boulder</div>
    <div class="hero-sub">Fast, Dependable Results When It Matters<br>The Most</div>
  </div>
  <div class="btn">Schedule Inspection</div>
  <div class="dots"><i></i><i></i><i></i></div>
</header>

<section class="about">
  <h2 class="heading">Environmental Testing Evolved</h2>
  <div class="about-text">
    <p>Lumaverde grew up in the rough and tumble disaster restoration industry. Time and time again, we saw projects small and large brought to a stand-still to await environmental testing and results.</p>
    <p>First, we had to know when it's prudent or even required by law to test for asbestos, lead-based paint, mold or other contaminants. Then we had to track down reliable testing companies, facilities or equipment. Next, we had to ensure we safeguarded people and property in the process of obtaining test samples. Finally, we had to wait, sometimes days or even weeks, while property owners languished and spent more and more money on expensive temporary living or working space. We just knew there had to be a better way.</p>
  </div>
  <div class="btn">Read More</div>
  <div class="about-photo" role="img" aria-label="Photo of an inspector in a protective suit beside a ladder on a weathered roof"></div>
</section>

<section class="project" role="region" aria-label="New construction project">
  <svg width="44" height="40" viewBox="0 0 44 40"><path d="M6 22a16 16 0 0 1 32 0z" fill="none" stroke="#fff" stroke-width="3"/><rect x="2" y="22" width="40" height="5" fill="#fff"/><rect x="20" y="5" width="4" height="10" fill="#fff"/></svg>
  <h2 class="heading">New Construction Project?</h2>
  <p>Let us start you in the right direction with our certified asbestos inspections ...Residential, commercial, schools, governmental properties, multi-family and more.</p>
  <div class="btn">Call Now</div>
</section>

<section class="services">
  <h2 class="heading">Our Services</h2>
  <div class="tabs"><span class="active">Asbestos Inspections</span><span>Mold Inspections</span><span>Lead Based Paint Testing</span></div>
  <p class="services-text">Lorem Ipsum is simply dummy text of the printing and typesetting industry. Lorem Ipsum has been the industry's standard dummy text ever since the 1500s, when an unknown printer took a galley of type and scrambled it to make a type specimen book. It has survived not only five centuries, but also the leap into electronic typesetting, remaining essentially unchanged. It was popularised in the 1960s with the release of Letterset sheets containing Lorem Ipsum passages, and more recently with desktop publishing software like Pagecraft including versions of Lorem Ipsum.</p>
  <div class="services-photo" role="img" aria-label="Photo of corrugated asbestos cement roofing sheets"></div>
</section>

<section class="why">
  <h2 class="heading">Why Choose Us</h2>
  <div class="reason" style="top:104px">
    <h3><svg width="30" height="24" viewBox="0 0 30 24"><path d="M2 12l9 9L28 3" stroke="#3d8fe0" stroke-width="4" fill="none"/></svg>We're serious about our work</h3>
    <p>We'll show up at your door with a smile and treat you like a new friend. But be assured that we're all business when it comes to delivering professional testing and consulting services.</p>
  </div>
  <div class="reason" style="top:218px">
    <h3><svg width="30" height="24" viewBox="0 0 30 24"><path d="M2 12l9 9L28 3" stroke="#3d8fe0" stroke-width="4" fill="none"/></svg>Fast, accurate test results. Very fast</h3>
    <p>For any environmental testing to be meaningful, much less valuable, you need the results to be reliable and fast. If it takes until mold spores become visible over a large area to get positive mold contamination test results, those results aren't really "news." They're "olds."</p>
  </div>
  <div class="reason" style="top:330px">
    <h3><svg width="30" height="24" viewBox="0 0 30 24"><path d="M2 12l9 9L28 3" stroke="#3d8fe0" stroke-width="4" fill="none"/></svg>We treat your family and business like ours</h3>
    <p>We never forget that our business is about people. Protecting people from hazards. When we enter your home or business, we consider how we would want to protect our home or business.</p>
  </div>
</section>

<section class="proof">
  <div class="card cert">
    <h2>Our Certificates</h2>
    <div class="badge" style="left:40px;top:80px;width:160px;height:56px;border-radius:6px"></div>
    <div class="badge" style="left:280px;top:76px;width:150px;height:66px;background:#a8a8a8"></div>
    <div class="badge" style="left:40px;top:166px;width:230px;height:96px;border-radius:48px 8px 8px 48px"></div>
    <div class="badge" style="left:390px;top:180px;width:70px;height:70px;border-radius:50%"></div>
    <div class="badge" style="left:135px;top:280px;width:235px;height:48px;background:#a8a8a8"></div>
  </div>
  <div class="card journey">
    <h2>Customer Journey</h2>
    <div class="date">2015/06/23</div>
    <div class="stars"><svg width="86" height="16" viewBox="0 0 86 16"><g fill="none" stroke="#6fb52c" stroke-width="1.3"><path id="s" d="M8 1l2 5h5l-4 3 2 5-5-3-5 3 2-5-4-3h5z"/><use href="#s" x="17"/><use href="#s" x="34"/><use href="#s" x="51"/><use href="#s" x="68"/></g></svg></div>
    <div class="quote">&ldquo;</div>
    <p>Lumaverde was a great help to us. They worked quickly to get our testing done so that we could continue our project. They were professional and prompt.</p>
    <div class="by">By <svg width="16" height="16"><circle cx="8" cy="8" r="7" fill="#0355a3"/></svg> a homeowner</div>
    <div class="btn">View Review</div>
  </div>
</section>

<section class="map" role="img" aria-label="Street map of the office location in Denver with a location pin"></section>

<footer class="footer">
  <div class="fcol" style="left:85px">
    <h4>Contact Info</h4>
    <ul class="contact">
      <li><svg width="12" height="16" viewBox="0 0 12 16"><path d="M6 0a6 6 0 0 1 6 6c0 4-6 10-6 10S0 10 0 6a6 6 0 0 1 6-6z" fill="#fff"/><circle cx="6" cy="6" r="2" fill="#0355a3"/></svg><span>2400 S. Harlow Ave. Ste. 210<br>Denver, Co. 80222</span></li>
      <li><svg width="14" height="14" viewBox="0 0 24 24"><path fill="#fff" d="M6.6 10.8a15 15 0 0 0 6.6 6.6l2.2-2.2c.3-.3.7-.4 1-.2 1.1.4 2.3.6 3.6.6.6 0 1 .4 1 1V20c0 .6-.4 1-1 1A17 17 0 0 1 3 4c0-.6.4-1 1-1h3.5c.6 0 1 .4 1 1 0 1.3.2 2.5.6 3.6.1.3 0 .7-.2 1z"/></svg>303-555-0147</li>
      <li><svg width="14" height="12" viewBox="0 0 20 16"><rect x="1" y="1" width="18" height="14" fill="#fff"/><path d="M1 1l9 7 9-7" stroke="#0355a3" stroke-width="2" fill="none"/></svg>info@trylumaverde.com</li>
    </ul>
  </div>
  <div class="fcol" style="left:399px">
    <h4>Social Links</h4>
    <ul>
      <li><svg width="12" height="12"><circle cx="6" cy="6" r="5" fill="#fff"/></svg>Facenote</li>
      <li><svg width="12" height="12"><circle cx="6" cy="6" r="5" fill="#fff"/></svg>Circleplus</li>
      <li><svg width="12" height="12"><circle cx="6" cy="6" r="5" fill="#fff"/></svg>Linkwork</li>
      <li><svg width="12" height="12"><circle cx="6" cy="6" r="5" fill="#fff"/></svg>Viewtube</li>
      <li><svg width="12" height="12"><circle cx="6" cy="6" r="5" fill="#fff"/></svg>Yapp</li>
    </ul>
  </div>
  <div class="fcol" style="left:594px">
    <h4>Quick Links</h4>
    <ul>
      <li><svg width="12" height="12"><circle cx="6" cy="6" r="5" fill="none" stroke="#fff" stroke-width="1.5"/><circle cx="6" cy="6" r="2" fill="#fff"/></svg>Home</li>
      <li><svg width="12" height="12"><circle cx="6" cy="6" r="5" fill="none" stroke="#fff" stroke-width="1.5"/><circle cx="6" cy="6" r="2" fill="#fff"/></svg>Our Services</li>
      <li><svg width="12" height="12"><circle cx="6" cy="6" r="5" fill="none" stroke="#fff" stroke-width="1.5"/><circle cx="6" cy="6" r="2" fill="#fff"/></svg>Resources</li>
      <li><svg width="12" height="12"><circle cx="6" cy="6" r="5" fill="none" stroke="#fff" stroke-width="1.5"/><circle cx="6" cy="6" r="2" fill="#fff"/></svg>Blog</li>
      <li><svg width="12" height="12"><circle cx="6" cy="6" r="5" fill="none" stroke="#fff" stroke-width="1.5"/><circle cx="6" cy="6" r="2" fill="#fff"/></svg>Q &amp; A</li>
      <li><svg width="12" height="12"><circle cx="6" cy="6" r="5" fill="none" stroke="#fff" stroke-width="1.5"/><circle cx="6" cy="6" r="2" fill="#fff"/></svg>Reviews</li>
    </ul>
  </div>
  <div class="fcol" style="left:790px;width:325px">
    <h4>Contact Form</h4>
    <div class="field">Name</div>
    <div class="field">Email</div>
    <div class="field message">Message</div>
    <div class="send"><svg width="14" height="14" viewBox="0 0 16 16"><path d="M1 8l14-7-4 14-3-5z" fill="#fff"/></svg></div>
  </div>
</footer>
<div class="legal">Lumaverde © 2017 | All Rights Reserved.</div>

</body>
</html>
```